Moden - Mexicali - Flower Shop

brisapetals is looking for a cool web design that has a airy, clean, mexicali feel to it.

See attached images and links for idea of what we mean with the above.

please no templates.
Updates

Target Market(s)

Local flower shop in San Diego, California

Industry/Entity Type

Shop

Requirements
Must have
• see. brisapetals.quillcart.example - I did the site and logo...I love the logo - hate the site.

Going for this feel: http://www.plumnotebook.example/tablecraft/archives/verandos.php

I also attached another site I liked- I just feel like it may be to busy.

```html
<!DOCTYPE html>
<html lang="en">
<head>
<meta charset="utf-8">
<title>Brisa Petals — Products</title>
<link rel="stylesheet" href="https://fonts.googleapis.com/css2?family=Fondamento&family=Noto+Serif:wght@400;700&display=swap">
<style>
:root{
  --page-purple:#3d1f57;
  --page-deep:#22102f;
  --gold:#d9b53a;
  --gold-soft:#b08a3a;
  --panel:#b8a7c4;
  --ink:#1c1224;
  --violet:#7a3fb0;
  --price-red:#e02b2b;
  --price-old:#3f6f74;
  --buy:#8a9268;
  --field:#8d7d99;
  --white:#ffffff;
  --footer-text:#f1ebf5;
}
*{box-sizing:border-box;margin:0;padding:0}
html,body{width:1095px;height:1200px;overflow:hidden;background:var(--page-purple)}
.canvas{position:relative;width:1095px;height:1200px;background:var(--page-purple);font-family:"Noto Serif",serif;color:var(--white)}
.abs{position:absolute}

/* navigation */
.main-nav a{position:absolute;font-family:"Fondamento",cursive;color:var(--gold);text-decoration:none;white-space:nowrap;line-height:1}
.nav-home{left:176px;top:14px;font-size:24px}
.nav-shop{left:157px;top:56px;font-size:37px}
.nav-curated{left:102px;top:116px;font-size:26px}
.nav-about{left:18px;top:163px;font-size:26px}

/* cart area */
.search-box{left:774px;top:17px;width:170px;height:22px;border-radius:4px;background:var(--field);display:flex;align-items:center;padding:0 6px;font-size:14px;color:var(--white)}
.search-box svg{margin-left:auto}
.cart-summary{left:959px;top:13px;font-size:18px;display:flex;gap:12px}
.cart-summary span{border-bottom:1px solid var(--white);line-height:1.15}
.view-cart{left:988px;top:46px;font-size:18px}

/* brand frame */
.brand-frame{left:380px;top:80px;width:334px;height:93px;border:1px solid var(--gold-soft);padding:5px}
.brand-card{width:100%;height:100%;background:var(--white);display:flex;align-items:center;justify-content:center;gap:14px;font-family:"Noto Serif",serif;font-size:25px;letter-spacing:5px;color:#6ea99b}
.brand-dot{width:28px;height:28px;border-radius:50%;background:#cfcfcf}

/* product panel */
.product-panel{left:147px;top:203px;width:803px;height:707px;border:1px solid var(--gold);padding:5px}
.panel-inner{position:relative;width:100%;height:100%;background:var(--panel);color:var(--ink)}
.panel-title{position:absolute;left:18px;top:14px;font-family:"Fondamento",cursive;font-size:37px;font-weight:400}
.filters{position:absolute;left:484px;top:5px;display:flex;align-items:center;gap:6px;font-family:"Fondamento",cursive;font-size:13px}
.select{width:69px;height:15px;background:#e4e0e8;border-radius:2px;font-family:Arial,sans-serif;font-size:9px;display:flex;align-items:center;justify-content:center;position:relative;margin-right:6px}
.select::after{content:"";position:absolute;right:5px;top:6px;border:3px solid transparent;border-top-color:var(--ink)}
.product{position:absolute;width:152px}
.product-photo{width:152px;height:152px}
.product-name{margin-top:15px;font-family:"Fondamento",cursive;font-size:13px;color:var(--violet)}
.product-row{display:flex;align-items:center;margin-top:4px;font-family:"Fondamento",cursive;font-size:12px}
.price-now{color:var(--price-red);margin-right:4px}
.price-was{color:var(--price-old);text-decoration:line-through}
.buy{margin-left:auto;width:44px;height:18px;background:var(--buy);color:#e8e8e0;text-align:center;line-height:18px;font-size:13px}

/* footer */
.footer-rule{left:0;top:933px;width:1095px;height:2px;background:var(--white)}
.site-footer{left:0;top:935px;width:1095px;height:265px;background:var(--page-deep)}
.footer-col{position:absolute;top:56px;font-size:14px;line-height:17.8px;color:var(--footer-text);letter-spacing:.3px}
.footer-col h3{font-size:14.5px;font-weight:700}
.col-meet{left:146px}
.col-reach{left:437px}
.col-news{left:710px}
.social{display:flex;gap:9px;margin-top:22px}
.social i{width:22px;height:22px;border-radius:50%;background:#d6d2d9}
.signup{position:absolute;left:709px;top:128px;display:flex;align-items:center;gap:11px}
.signup-field{width:177px;height:22px;background:var(--field);padding-left:6px;font-size:14px;line-height:22px;color:var(--white)}
.signup-btn{font-size:14px;color:#cfc6d6}
.copyright{position:absolute;left:0;width:1095px;top:235px;text-align:center;font-size:14px;color:#a99cb3}
.base-strip{left:0;top:1188px;width:1095px;height:12px;background:#0b0710}
</style>
</head>
<body>
<div class="canvas">

  <nav class="main-nav">
    <a class="nav-home" href="#">Home</a>
    <a class="nav-shop" href="#">Shop</a>
    <a class="nav-curated" href="#">Curated</a>
    <a class="nav-about" href="#">About Us</a>
  </nav>

  <div class="abs search-box">Search Store
    <svg width="14" height="14" viewBox="0 0 14 14"><circle cx="5.5" cy="5.5" r="4.3" fill="none" stroke="#fff" stroke-width="1.4"/><line x1="8.6" y1="8.6" x2="13" y2="13" stroke="#fff" stroke-width="1.6"/></svg>
  </div>
  <div class="abs cart-summary"><span>0 items</span><span>$0.0</span></div>
  <div class="abs view-cart">View Cart</div>

  <div class="abs brand-frame">
    <div class="brand-card"><span class="brand-dot"></span>BRISA PETALS</div>
  </div>

  <section class="abs product-panel">
    <div class="panel-inner">
      <h1 class="panel-title">Products</h1>
      <div class="filters">
        <span>Sort By</span><span class="select">A to Z</span>
        <span>Browse By tag</span><span class="select">All</span>
      </div>

      <article class="product" style="left:19px;top:83px">
        <div class="product-photo" role="img" aria-label="Bouquet of orange and yellow lilies wrapped in paper" style="background:linear-gradient(135deg,#8a8078,#d88a2a 45%,#e6c24a 60%,#6a8a3a)"></div>
        <div class="product-name">California Lillies</div>
        <div class="product-row"><span class="price-now">$ 50.00</span><span class="price-was">$ 75.00</span><span class="buy">Buy</span></div>
      </article>
      <article class="product" style="left:201px;top:83px">
        <div class="product-photo" role="img" aria-label="White calla lilies on a grey wooden table" style="background:linear-gradient(135deg,#6c6c6a,#d8d8d2 45%,#5c7a3a 75%,#4e4e4c)"></div>
        <div class="product-name">Guy flowers</div>
        <div class="product-row"><span class="price-now">$ 40.00</span><span class="price-was">$ 70.00</span><span class="buy">Buy</span></div>
      </article>
      <article class="product" style="left:382px;top:85px">
        <div class="product-photo" role="img" aria-label="Pile of deep red roses on wooden boards" style="background:linear-gradient(160deg,#7a1020,#a0182a 55%,#8a8580)"></div>
        <div class="product-name">Ruby Roses</div>
        <div class="product-row"><span class="price-now">$ 40.00</span><span class="price-was">$ 75.00</span><span class="buy">Buy</span></div>
      </article>
      <article class="product" style="left:560px;top:83px">
        <div class="product-photo" role="img" aria-label="Pink gerbera bouquet in kraft paper" style="background:linear-gradient(160deg,#8a8a88,#c89a6a 35%,#e06a8a 50%,#5f8a3a 80%)"></div>
        <div class="product-name">Spring time</div>
        <div class="product-row"><span class="price-now">$ 50.00</span><span class="price-was">$ 60.00</span><span class="buy">Buy</span></div>
      </article>
      <article class="product" style="left:20px;top:313px">
        <div class="product-photo" role="img" aria-label="Orange sunflowers wrapped in kraft paper" style="background:linear-gradient(160deg,#8a8884,#e0601a 35%,#c8501a 55%,#b89a6a 85%)"></div>
        <div class="product-name">Sun Flowers</div>
        <div class="product-row"><span class="price-now">$ 50.00</span><span class="price-was">$ 75.00</span><span class="buy">Buy</span></div>
      </article>
    </div>
  </section>

  <div class="abs footer-rule"></div>
  <footer class="abs site-footer">
    <div class="footer-col col-meet">
      <h3>Meet Brisa</h3>
      <p>Based in Hillcrest, San Diego<br>We offer farm fresh, curated,<br>cool, and same day delivery<br>flower bouquets.</p>
      <div class="social"><i></i><i></i><i></i></div>
    </div>
    <div class="footer-col col-reach">
      <h3>Reach Brisa</h3>
      <p>2218 Marlow Avenue<br>San Diego, CA 92103<br>Email: hello@brisapetals.example<br>Phone: 619-555-0143</p>
    </div>
    <div class="footer-col col-news">
      <h3>Newsletter</h3>
      <p>We promise to only send you<br>good things like discounts!</p>
    </div>
    <div class="signup"><span class="signup-field">your@email.com</span><span class="signup-btn">Sign up</span></div>
    <p class="copyright">Copyright © 2014 brisapetals of San Diego.</p>
  </footer>
  <div class="abs base-strip"></div>
</div>
</body>
</html>
```